Gin Bottle label

Hi, I would like a design based on a traditional, Vintage, Victorian type label.
The product is 'Thistle & Marrowroot Gin'
It will be 50cl and 40% vol.
The Gin will be dark brown in colour and attached is the types of bottle and a few ideas of the styles I like.
Many Thanks

```html
<!DOCTYPE html>
<html lang="en">
<head>
<meta charset="utf-8">
<title>Thistle &amp; Marrowroot Gin – Label</title>
<link rel="stylesheet" href="https://fonts.googleapis.com/css2?family=Rye&family=Oswald:wght@500;600&display=swap">
<style>
  :root {
    --olive: #8a7a4c;
    --olive-dark: #7a6b40;
    --ring: #d2cab8;
    --paper: #ffffff;
    --backdrop: #f3f3f3;
  }
  html, body {
    margin: 0;
    padding: 0;
    width: 1200px;
    height: 794px;
    overflow: hidden;
    background: var(--backdrop);
  }
  .label-canvas { display: block; width: 1200px; height: 794px; }
  .arc-text {
    font-family: "Oswald", sans-serif;
    font-weight: 600;
    font-size: 16px;
    letter-spacing: 3px;
    fill: var(--olive);
  }
  .abv-text {
    font-family: "Oswald", sans-serif;
    font-weight: 600;
    font-size: 19px;
    letter-spacing: 1px;
    fill: var(--olive-dark);
  }
  .brand-main {
    font-family: "Rye", serif;
    font-size: 38px;
    letter-spacing: 3px;
    fill: var(--paper);
  }
  .brand-sub {
    font-family: "Rye", serif;
    font-size: 27px;
    letter-spacing: 1px;
    fill: var(--paper);
  }
  .product-type {
    font-family: "Rye", serif;
    font-size: 42px;
    letter-spacing: 2px;
    fill: var(--olive-dark);
  }
  .volume-text {
    font-family: "Oswald", sans-serif;
    font-weight: 600;
    font-size: 15px;
    fill: var(--paper);
  }
  .star { fill: var(--paper); }
</style>
</head>
<body>
<svg class="label-canvas" viewBox="0 0 1200 794" xmlns="http://www.w3.org/2000/svg">
  <defs>
    <clipPath id="label-inner">
      <ellipse cx="600" cy="397" rx="212" ry="292"/>
    </clipPath>
    <linearGradient id="illustration-tone" x1="0" y1="0" x2="0" y2="1">
      <stop offset="0" stop-color="#efeadf"/>
      <stop offset="1" stop-color="#c9bd9b"/>
    </linearGradient>
    <path id="top-arc" d="M 410 397 A 190 270 0 0 1 790 397"/>
  </defs>

  <g class="gin-label">
    <!-- outer frame -->
    <ellipse cx="600" cy="397" rx="250" ry="330" fill="var(--olive)"/>
    <ellipse cx="600" cy="397" rx="244" ry="324" fill="var(--ring)"/>
    <ellipse class="dot-ring" cx="600" cy="397" rx="230" ry="310" fill="none"
             stroke="var(--paper)" stroke-width="4.5" stroke-linecap="round" stroke-dasharray="0 14"/>
    <ellipse cx="600" cy="397" rx="218" ry="298" fill="var(--olive)"/>
    <ellipse cx="600" cy="397" rx="212" ry="292" fill="var(--paper)"/>
    <ellipse cx="600" cy="397" rx="172" ry="250" fill="none" stroke="var(--olive)" stroke-width="2"/>

    <!-- arc slogan -->
    <text class="arc-text"><textPath href="#top-arc" startOffset="50%" text-anchor="middle">DISTILLED IN THE BEST WAY</textPath></text>

    <!-- illustration area -->
    <rect class="illustration" x="455" y="222" width="290" height="188" rx="4"
          fill="url(#illustration-tone)" role="img"
          aria-label="Engraved vintage steam fire engine with large spoked wheels"/>

    <!-- strength banner -->
    <g class="abv-banner" transform="rotate(-8 686 252)">
      <rect x="626" y="235" width="120" height="34" fill="var(--paper)" stroke="var(--olive)" stroke-width="2"/>
      <text class="abv-text" x="686" y="259" text-anchor="middle">40% VOL.</text>
    </g>

    <!-- name band -->
    <g clip-path="url(#label-inner)">
      <rect class="name-band" x="370" y="428" width="460" height="96" fill="var(--olive)"/>
    </g>
    <polygon class="star" points="411,450 414,459 423,459 416,465 419,474 411,468 403,474 406,465 399,459 408,459"/>
    <polygon class="star" points="789,450 792,459 801,459 794,465 797,474 789,468 781,474 784,465 777,459 786,459"/>
    <text class="brand-main" x="600" y="472" text-anchor="middle">THISTLE</text>
    <text class="brand-sub" x="600" y="511" text-anchor="middle">&amp; MARROWROOT</text>

    <!-- product type banner -->
    <rect x="432" y="526" width="40" height="50" fill="var(--ring)" stroke="var(--olive)" stroke-width="2"/>
    <rect x="728" y="526" width="40" height="50" fill="var(--ring)" stroke="var(--olive)" stroke-width="2"/>
    <rect class="type-banner" x="468" y="534" width="264" height="56" rx="3"
          fill="var(--paper)" stroke="var(--olive)" stroke-width="2.5"/>
    <text class="product-type" x="600" y="578" text-anchor="middle">GIN</text>

    <!-- volume seal -->
    <circle cx="600" cy="618" r="22" fill="var(--olive)"/>
    <text class="volume-text" x="600" y="624" text-anchor="middle">50CL</text>
    <line x1="585" y1="648" x2="615" y2="648" stroke="var(--olive)" stroke-width="2"/>
    <line x1="590" y1="654" x2="610" y2="654" stroke="var(--olive)" stroke-width="2"/>
  </g>
</svg>
</body>
</html>
```